Letterhead for new real estate company in South Africa named Tallowick

A letterhead with the directors and company details to be editable as these changes often

Target Market(s)

In line with our logo brief and our newly designed logo and corporate fee

Industry/Entity Type

Real Estate

Requirements
Must have
• Details as per the sample letterhead provided.

```html
<!DOCTYPE html>
<html lang="en">
<head>
<meta charset="utf-8">
<title>Tallowick Letterhead</title>
<link href="https://fonts.googleapis.com/css2?family=Poppins:ital,wght@0,400;0,500;1,400&display=swap" rel="stylesheet">
<style>
  :root {
    --backdrop: #e4e4e4;
    --paper-light: #f3f3f3;
    --paper: #ebebeb;
    --brand-green: #2eaa66;
    --ink: #1e1e1e;
    --ink-soft: #333333;
  }
  html, body {
    margin: 0;
    padding: 0;
    width: 960px;
    height: 1200px;
    overflow: hidden;
    background: var(--backdrop);
    font-family: "Poppins", sans-serif;
  }
  .letterhead {
    position: absolute;
    left: 67px;
    top: 20px;
    width: 826px;
    height: 1160px;
    background: linear-gradient(90deg, var(--paper-light) 0%, var(--paper) 60%);
    box-shadow: 0 2px 10px rgba(0,0,0,0.12);
  }
  .brand {
    position: absolute;
    left: 75px;
    top: 76px;
    display: flex;
    align-items: center;
    gap: 12px;
  }
  .brand-dot {
    width: 22px;
    height: 22px;
    border-radius: 50%;
    background: var(--brand-green);
  }
  .brand-name {
    font-size: 33px;
    font-weight: 400;
    color: var(--brand-green);
    letter-spacing: 0.5px;
    line-height: 1;
  }
  .contact {
    position: absolute;
    left: 494px;
    top: 65px;
    height: 82px;
    border-left: 2px solid var(--brand-green);
    padding-left: 19px;
    color: var(--ink);
    font-size: 14px;
    line-height: 16.5px;
  }
  .contact p { margin: 0; }
  .contact .street { font-size: 13px; letter-spacing: -0.5px; }
  .contact .line {
    display: flex;
    align-items: center;
    gap: 6px;
  }
  .contact .line.first { margin-top: 5px; }
  .contact svg { width: 11px; height: 11px; flex: none; }
  .footer {
    position: absolute;
    left: 0;
    right: 0;
    top: 1084px;
    text-align: center;
    font-size: 13.5px;
    line-height: 18px;
  }
  .footer .directors { margin: 0; color: var(--brand-green); }
  .footer .notice { margin: 0; color: var(--ink-soft); font-style: italic; }
</style>
</head>
<body>
  <div class="letterhead">
    <div class="brand">
      <span class="brand-dot"></span>
      <span class="brand-name">TALLOWICK</span>
    </div>

    <div class="contact">
      <p>Suite 12B, Marlow Square</p>
      <p class="street">Corner Kestrel Avenue &amp; Finch Road</p>
      <p>Hartvale, South Africa</p>
      <p class="line first">
        <svg viewBox="0 0 24 24" aria-hidden="true"><path fill="#2eaa66" d="M6.6 10.8a15.1 15.1 0 0 0 6.6 6.6l2.2-2.2c.3-.3.7-.4 1-.2 1.1.4 2.3.6 3.6.6.6 0 1 .4 1 1V20c0 .6-.4 1-1 1A17 17 0 0 1 3 4c0-.6.4-1 1-1h3.5c.6 0 1 .4 1 1 0 1.3.2 2.5.6 3.6.1.3 0 .7-.2 1z"/></svg>
        <span>087 555 0142</span>
      </p>
      <p class="line">
        <svg viewBox="0 0 24 24" aria-hidden="true"><circle cx="12" cy="12" r="10" fill="#2eaa66"/><path d="M2 12h20M12 2c3 3 3 17 0 20M12 2c-3 3-3 17 0 20" stroke="#ebebeb" stroke-width="1.6" fill="none"/></svg>
        <span>tallowick.co.za</span>
      </p>
    </div>

    <div class="footer">
      <p class="directors">Directors: T Vermaak / GA Lindqvist-Rowe</p>
      <p class="notice">Each franchise is independently owned &amp; operated</p>
    </div>
  </div>
</body>
</html>
```